Business Card for By Karel Voss

Looking to have a business card designed for my lifestyle and fitness company. My company offers personal training, online programming and nutrition advice based out of London, United Kingdom.

I'd like to see modern, sleek designs, focusing on black, matte black or matte grey. Design doesn't need to be overly descriptive as this will also be used as a personal business card. I've included my logo.

Please note that my company is no longer called "Fitness by Karel Voss" but instead "By Karel Voss", this is because of my other ventures. Therefore please don't use the "fitness by karel voss" text.

information about my company can be found at www.bykarelvoss.com

Company is also based out of London (United Kingdom) & Sydney (Australia) this could be reflected on the card.

Industry/Entity Type

Business

Contact Information for Business Card

Karel Voss
+44 7382 615027
karel@bykarelvoss.com
www.bykarelvoss.com

Font styles to use
Sans Serif

Requirements
Must have
• All contact details and inclusion of my logo.

```html
<!DOCTYPE html>
<html lang="en">
<head>
<meta charset="UTF-8">
<title>By Karel Voss — Business Card</title>
<link rel="stylesheet" href="https://fonts.googleapis.com/css2?family=Montserrat:wght@400;500;700&display=swap">
<style>
  :root {
    --page-bg: #d9d6d2;
    --card-dark: #262626;
    --card-mid: #333333;
    --ink: #f2f2f2;
    --ink-soft: #c9c9c9;
    --rule: #e6e6e6;
  }
  * { margin: 0; padding: 0; box-sizing: border-box; }
  html, body {
    width: 1200px; height: 900px; overflow: hidden;
    background: var(--page-bg);
    font-family: "Montserrat", sans-serif;
  }
  .sheet {
    width: 1200px; height: 900px;
    display: flex; flex-direction: column; align-items: center; justify-content: center;
    gap: 40px;
  }
  .card {
    position: relative;
    width: 680px; height: 388px;
    background: radial-gradient(ellipse at 60% 40%, var(--card-mid) 0%, var(--card-dark) 75%);
    color: var(--ink);
    overflow: hidden;
    box-shadow: 0 10px 28px rgba(0,0,0,0.28);
  }
  .card-rules { position: absolute; inset: 0; width: 100%; height: 100%; }
  .card-rules line { stroke: var(--rule); stroke-width: 1.6; }

  /* Brand name placeholder: plain text with one circle */
  .brand {
    position: absolute;
    display: flex; align-items: center; gap: 12px;
    font-weight: 400; color: var(--ink);
    white-space: nowrap; line-height: 1;
  }
  .brand-dot { background: var(--ink); border-radius: 50%; flex: none; }
  .front .brand { left: 440px; top: 124px; font-size: 24px; }
  .front .brand-dot { width: 14px; height: 14px; }
  .back .brand { left: 360px; top: 156px; font-size: 32px; }
  .back .brand-dot { width: 18px; height: 18px; }

  /* Front: identity + contacts */
  .identity { position: absolute; left: 48px; top: 166px; }
  .identity-name { font-size: 22px; font-weight: 400; color: var(--ink); line-height: 1; }
  .identity-name strong { font-weight: 700; }
  .identity-role { margin-top: 7px; font-size: 14px; font-weight: 400; color: var(--ink-soft); letter-spacing: 0.5px; }
  .identity-bar { margin-top: 9px; width: 70px; height: 4px; background: var(--ink); }

  .contacts { position: absolute; left: 48px; top: 246px; list-style: none; }
  .contacts li {
    display: flex; align-items: center; gap: 14px;
    height: 30px; font-size: 15px; color: var(--ink-soft); letter-spacing: 0.3px;
  }
  .contacts svg { width: 16px; height: 16px; flex: none; fill: var(--ink); }

  /* Back: web address */
  .web-line {
    position: absolute; left: 340px; top: 262px;
    font-size: 15px; font-weight: 500; letter-spacing: 5px; color: var(--ink-soft);
    white-space: nowrap; line-height: 18px;
  }
</style>
</head>
<body>
<main class="sheet">

  <section class="card front" aria-label="Business card front">
    <svg class="card-rules" viewBox="0 0 680 388" aria-hidden="true">
      <line x1="0" y1="78" x2="395" y2="78"/>
      <line x1="640" y1="78" x2="680" y2="78"/>
      <line x1="0" y1="180" x2="36" y2="180"/>
      <line x1="180" y1="180" x2="680" y2="180"/>
      <line x1="0" y1="348" x2="36" y2="348"/>
      <line x1="60" y1="348" x2="680" y2="348"/>
    </svg>

    <div class="brand"><span class="brand-dot"></span>By Karel Voss</div>

    <div class="identity">
      <p class="identity-name"><strong>Karel</strong> Voss</p>
      <p class="identity-role">Managing Director</p>
      <div class="identity-bar"></div>
    </div>

    <ul class="contacts">
      <li>
        <svg viewBox="0 0 24 24" aria-hidden="true"><path d="M6.6 10.8c1.4 2.8 3.8 5.1 6.6 6.6l2.2-2.2c.3-.3.7-.4 1-.2 1.1.4 2.3.6 3.6.6.6 0 1 .4 1 1V20c0 .6-.4 1-1 1C10.6 21 3 13.4 3 4c0-.6.4-1 1-1h3.5c.6 0 1 .4 1 1 0 1.3.2 2.5.6 3.6.1.3 0 .7-.2 1z"/></svg>
        +44 7382 615027
      </li>
      <li>
        <svg viewBox="0 0 24 24" aria-hidden="true"><path d="M2 5h20v14H2z M4 7v.4l8 5.2 8-5.2V7z" fill-rule="evenodd"/></svg>
        karel@bykarelvoss.com
      </li>
      <li>
        <svg viewBox="0 0 24 24" aria-hidden="true"><path d="M12 2a10 10 0 1 0 0 20 10 10 0 0 0 0-20zm6.9 6h-3a15 15 0 0 0-1.3-3.9A8 8 0 0 1 18.9 8zM12 4c.8 1.1 1.5 2.5 1.9 4h-3.8c.4-1.5 1.1-2.9 1.9-4zM4.3 14a8 8 0 0 1 0-4h3.4a16 16 0 0 0 0 4zm.8 2h3a15 15 0 0 0 1.3 3.9A8 8 0 0 1 5.1 16zm3-8h-3a8 8 0 0 1 4.3-3.9A15 15 0 0 0 8.1 8zM12 20c-.8-1.1-1.5-2.5-1.9-4h3.8c-.4 1.5-1.1 2.9-1.9 4zm2.3-6H9.7a14 14 0 0 1 0-4h4.6a14 14 0 0 1 0 4zm.3 5.9a15 15 0 0 0 1.3-3.9h3a8 8 0 0 1-4.3 3.9zm1.7-5.9a16 16 0 0 0 0-4h3.4a8 8 0 0 1 0 4z"/></svg>
        www.bykarelvoss.com
      </li>
    </ul>
  </section>

  <section class="card back" aria-label="Business card back">
    <svg class="card-rules" viewBox="0 0 680 388" aria-hidden="true">
      <line x1="600" y1="40" x2="680" y2="40"/>
      <line x1="330" y1="212" x2="640" y2="212"/>
      <line x1="230" y1="271" x2="325" y2="271"/>
      <line x1="625" y1="271" x2="680" y2="271"/>
      <line x1="0" y1="350" x2="260" y2="350"/>
    </svg>

    <div class="brand"><span class="brand-dot"></span>By Karel Voss</div>

    <p class="web-line">www.bykarelvoss.com</p>
  </section>

</main>
</body>
</html>
```